Amber Burrows Business Card Design

Amber Burrows - Gathering Gentle Meadow Corners

Amber Burrows is a company that focuses on promoting the design, construction, consultation and support of natural, creative and organic play spaces for Early Childhood and learning environments.

We need a professional Business Card designed that is unique modern and creative. The Philosophy of the company is nostalgic so the business and will need to reflect this but also reflect that our ideas are modern and cutting edge.

The business card will need to be a talking point, by either having a unique size, quality and/or placement of logo or other quality.

I am more interested in using natural recycled paper, as this would reflect the philosophy of the company, but I open to seeing colour used creatively.
Updates

Hi Designers, Apologies, Could you please add www.amberburrows.com.au to the business card. Thanks very much.

Hi All, Thank you all for your submission thus far. Please note the fonts for used in the logo are: Ostrich Sans Black and Archer Semi Bold. If these could be considered for contact details, my name etc. Also please show the design on a recycled brown card if possible as this will be the type of card I will use when printing. Thanks so much.

Target Market(s)

Child Care Providers, Play Industry Professionals

Industry/Entity Type

Business

Contact Information for Business Card

Amber Burrows
Gathering Gentle Meadow Corners
Marguerite Holloway
0419 862 503
marguerite@amberburrows.com.au

Font styles to use
Sans Serif

Requirements
Must have
• The Logo and the Details plus the below phrase
• Amber Burrows - Gathering Gentle Meadow Corners
Nice to have
• A bit of colour, but not too much colour.
Should not have
• Not to have a white background, recycled brown card only

```html
<!DOCTYPE html>
<html lang="en">
<head>
<meta charset="utf-8">
<title>Amber Burrows Business Card Design</title>
<link rel="stylesheet" href="https://fonts.googleapis.com/css2?family=Montserrat:wght@300;400;500;700&family=Cinzel:wght@400;700&display=swap">
<style>
  :root {
    --backdrop: #e9e6e1;
    --kraft-light: #d4a867;
    --kraft-mid: #c99a58;
    --kraft-deep: #b8864a;
    --ink: #3b2414;
    --ink-soft: #4a2f1c;
  }
  * { box-sizing: border-box; margin: 0; padding: 0; }
  html, body {
    width: 1200px; height: 918px; overflow: hidden;
    background: var(--backdrop);
  }
  .canvas {
    width: 1200px; height: 918px;
    display: flex; align-items: center; justify-content: center; gap: 40px;
  }
  .card {
    position: relative;
    width: 540px; height: 309px;
    overflow: hidden;
    color: var(--ink);
    background:
      radial-gradient(circle at 30% 25%, rgba(255,230,180,0.35), transparent 55%),
      radial-gradient(circle at 80% 80%, rgba(150,100,40,0.25), transparent 60%),
      linear-gradient(135deg, var(--kraft-light), var(--kraft-mid) 55%, var(--kraft-deep));
    box-shadow: 0 6px 18px rgba(0,0,0,0.18);
  }

  /* Front: brand side */
  .card-front {
    display: flex; flex-direction: column; align-items: center; justify-content: center;
    text-align: center;
  }
  .brand-emblem {
    width: 130px; height: 104px;
    border-radius: 50% 50% 12% 12%;
    background: radial-gradient(ellipse at 50% 40%, var(--ink-soft), var(--ink));
    margin-bottom: 14px;
  }
  .brand-name {
    font-family: 'Montserrat', sans-serif;
    font-weight: 700;
    font-size: 24px;
    letter-spacing: 2px;
  }
  .brand-tagline {
    font-family: 'Cinzel', serif;
    font-size: 12px;
    letter-spacing: 1.5px;
    margin-top: 6px;
  }
  .brand-rule {
    width: 90px; height: 1px; background: var(--ink);
    margin: 12px 0 10px;
  }
  .brand-web {
    font-family: 'Cinzel', serif;
    font-size: 12px;
    letter-spacing: 0.5px;
  }

  /* Back: contact side */
  .accent-line {
    position: absolute; left: 40px; top: 0;
    width: 3px; height: 120px;
    background: var(--ink);
  }
  .contact {
    position: absolute; left: 52px; top: 132px;
    font-family: 'Montserrat', sans-serif;
  }
  .person-name {
    font-size: 24px; font-weight: 300; letter-spacing: 0.5px; line-height: 1;
    text-transform: uppercase;
  }
  .person-name strong { font-weight: 700; }
  .person-role { font-size: 11px; font-weight: 500; margin-top: 2px; }
  .contact-list { list-style: none; margin-top: 14px; }
  .contact-item {
    display: flex; align-items: flex-start; gap: 12px;
    font-size: 12.5px; font-weight: 500; line-height: 1.3;
    margin-bottom: 9px;
  }
  .contact-icon { width: 14px; height: 14px; flex: none; margin-top: 1px; fill: var(--ink); }
  .tree-illustration {
    position: absolute; right: 0; top: 16px;
    width: 160px; height: 293px;
    border-radius: 60% 10% 0 30% / 35% 5% 0 20%;
    background: linear-gradient(180deg, var(--ink-soft), var(--ink));
  }
</style>
</head>
<body>
<main class="canvas">
  <section class="card card-front" aria-label="Card front">
    <div class="brand-emblem" role="img" aria-label="Tree silhouette emblem illustration"></div>
    <div class="brand-name">AMBER BURROWS</div>
    <div class="brand-tagline">GATHERING GENTLE MEADOW CORNERS</div>
    <div class="brand-rule"></div>
    <div class="brand-web">www.amberburrows.com.au</div>
  </section>

  <section class="card card-back" aria-label="Card back">
    <div class="accent-line"></div>
    <div class="contact">
      <h1 class="person-name">Marguerite <strong>Holloway</strong></h1>
      <p class="person-role">Manager</p>
      <ul class="contact-list">
        <li class="contact-item">
          <svg class="contact-icon" viewBox="0 0 24 24"><path d="M12 2a7 7 0 0 0-7 7c0 5 7 13 7 13s7-8 7-13a7 7 0 0 0-7-7zm0 9.5A2.5 2.5 0 1 1 12 6.5a2.5 2.5 0 0 1 0 5z"/></svg>
          <span>2847 Fern Hollow Road<br>Millbrook, ME 04211</span>
        </li>
        <li class="contact-item">
          <svg class="contact-icon" viewBox="0 0 24 24"><path d="M6.6 10.8a15 15 0 0 0 6.6 6.6l2.2-2.2a1 1 0 0 1 1-.25 11 11 0 0 0 3.6.6 1 1 0 0 1 1 1V20a1 1 0 0 1-1 1A17 17 0 0 1 3 4a1 1 0 0 1 1-1h3.5a1 1 0 0 1 1 1c0 1.25.2 2.45.6 3.6a1 1 0 0 1-.25 1z"/></svg>
          <span>0419 862 503</span>
        </li>
        <li class="contact-item">
          <svg class="contact-icon" viewBox="0 0 24 24"><path d="M2 5h20v14H2zm2 2v.5l8 5 8-5V7l-8 5z"/></svg>
          <span>marguerite@amberburrows.com.au</span>
        </li>
      </ul>
    </div>
    <div class="tree-illustration" role="img" aria-label="Leafy tree silhouette illustration rising from the card corner"></div>
  </section>
</main>
</body>
</html>
```